Commercial janitorial cleaning

Janitorial cleaning particularly for commercial buildings. Website needs to specify free estimates. Location of service is Hudson, Valatie, East Greenbush, Troy, Albany ny area. Services page with Janitorial services- General Office Cleaning, Construction Cleaning, Carpet Extraction, Consultation/Business, Lighting Maintenance, Seasonal Deep Cleaning, Window cleaning, Event Cleaning, Floor and Carpet Cleaning, Floor Striping and Waxing. Contact us page with email phone number on page and a request page that emails me if they have any questions. About us page-the picture of my family on it with a section I can type a story myself.

Target Market(s)

Commercial businesses

Industry/Entity Type

Janitorial Service

Number of Pages Required

4 page

Font styles to use
Serif
Sans Serif
Script

Colors
ec1f27
1b1b1b
ffffff
9d9d9d

Requirements
Must have
• Phone number 555-314-2760. Must have free estimates on home page. Going for industrial / modern look to website
Nice to have
• Logo is a red and black building so if those colors could be coordinated to website that would be awesome.

```html
<!DOCTYPE html>
<html lang="en">
<head>
<meta charset="utf-8">
<title>Steadfast Cleaning Services – Commercial Janitorial Cleaning</title>
<link href="https://fonts.googleapis.com/css2?family=Open+Sans:wght@300;400;600;700&display=swap" rel="stylesheet">
<style>
:root{
  --red:#ec1f27;
  --ink:#1b1b1b;
  --white:#ffffff;
  --grey:#9d9d9d;
  --text:#555555;
  --soft:#f5f5f5;
  --line:#dddddd;
  --footer:#2b2b2b;
  --blue:#2f8fd8;
  --green:#5cb531;
}
*{margin:0;padding:0;box-sizing:border-box}
html,body{width:1200px;height:2927px;overflow:hidden;background:var(--white)}
body{font-family:"Open Sans",Arial,sans-serif;color:var(--ink);position:relative}
section,header,footer{position:absolute;left:0;width:1200px}
.center{text-align:center}
.btn{display:inline-block;background:var(--red);color:var(--white);text-transform:uppercase;font-weight:600;text-decoration:none}

/* header */
.site-header{top:0;height:146px;background:var(--white)}
.brand{position:absolute;left:98px;top:14px;width:160px;text-align:center}
.brand-mark{display:block;width:28px;height:28px;background:var(--red);margin:0 auto 10px}
.brand-name{font-size:19px;font-weight:400;letter-spacing:.5px;color:var(--ink);line-height:1.1}
.brand-sub{font-size:12.5px;letter-spacing:1px;color:var(--ink)}
.call{position:absolute;left:616px;top:20px;display:flex;align-items:center;gap:10px;font-size:27px;font-weight:300;color:#333}
.call .num{color:var(--ink);font-weight:400}
.header-estimate{position:absolute;left:976px;top:24px;width:125px;height:37px;line-height:37px;text-align:center;font-size:13px;font-weight:400}
.nav{position:absolute;top:84px;left:440px;display:flex;gap:0;list-style:none;font-size:14.5px;color:#444}
.nav li{position:absolute;white-space:nowrap}
.nav li.active{color:var(--red)}
.nav li.active::after{content:"";position:absolute;left:-4px;right:-4px;top:30px;height:2px;background:var(--red)}

/* hero */
.hero{top:146px;height:578px;background:linear-gradient(180deg,#7d7a6e 0%,#5e5b52 50%,#474540 100%);overflow:hidden}
.hero-photo{position:absolute;inset:0;background:radial-gradient(ellipse at 30% 60%,rgba(240,200,30,.85) 0%,rgba(220,180,20,.55) 28%,rgba(0,0,0,0) 55%),radial-gradient(ellipse at 80% 50%,rgba(240,200,30,.8) 0%,rgba(200,160,20,.4) 30%,rgba(0,0,0,0) 55%)}
.hero h1{position:absolute;top:196px;width:100%;text-align:center;color:var(--white);font-size:37px;font-weight:700;letter-spacing:.5px;text-shadow:0 2px 6px rgba(0,0,0,.5)}
.hero p{position:absolute;top:253px;width:100%;text-align:center;color:var(--white);font-size:23px;text-shadow:0 2px 6px rgba(0,0,0,.5)}
.hero .btn{position:absolute;left:504px;top:329px;width:190px;height:45px;line-height:45px;text-align:center;font-size:19px;font-weight:400;letter-spacing:.5px}
.slide-arrow{position:absolute;top:266px;width:38px;height:46px}
.slide-arrow.prev{left:24px}
.slide-arrow.next{right:0}

/* welcome */
.welcome{top:724px;height:534px}
.section-title{font-size:31px;font-weight:300;color:var(--ink);text-align:center;text-transform:uppercase}
.welcome .section-title{position:absolute;top:60px;width:100%}
.welcome .intro{position:absolute;top:118px;left:140px;width:920px;font-size:13.5px;line-height:25px;color:var(--grey);text-align:center}
.feature{position:absolute;top:210px;width:320px;text-align:center}
.feature .disc{width:146px;height:146px;border-radius:50%;margin:0 auto;border:4px solid var(--white);box-shadow:0 0 0 2px currentColor;display:flex;align-items:center;justify-content:center}
.feature h3{margin-top:24px;font-size:24px;font-weight:300;text-transform:uppercase;color:var(--ink)}
.feature p{margin-top:8px;font-size:14px;line-height:23px;color:var(--grey);padding:0 18px}

/* services */
.services{top:1258px;height:478px;background:var(--soft)}
.services .section-title{position:absolute;top:42px;width:100%}
.pager{position:absolute;top:53px;left:1056px;display:flex;gap:4px}
.pager span{width:20px;height:20px;background:#333;display:block}
.card{position:absolute;top:119px;width:242px;height:276px;background:var(--white);box-shadow:0 18px 18px -14px rgba(0,0,0,.25)}
.card .thumb{height:166px}
.card h4{margin:20px 16px 0;font-size:16.5px;font-weight:400;text-transform:uppercase;color:var(--ink)}
.card p{margin:8px 16px 0;font-size:11.5px;line-height:19px;color:var(--grey)}

/* about */
.about{top:1736px;height:504px}
.about .section-title{position:absolute;top:40px;width:100%}
.about-copy{position:absolute;left:100px;top:122px;width:490px}
.about-copy h3{font-size:19.5px;font-weight:400;text-transform:uppercase;color:var(--ink)}
.about-copy .lead{margin-top:18px;font-size:13px;line-height:23px;color:#555}
.ticks{list-style:none;margin-top:18px}
.ticks li{display:flex;align-items:center;gap:14px;font-size:13px;color:#555;height:35px}
.about .btn{position:absolute;left:100px;top:387px;width:152px;height:45px;line-height:45px;text-align:center;font-size:16px;font-weight:400;border-radius:2px}
.family-photo{position:absolute;left:616px;top:125px;width:486px;height:307px;border-radius:4px;background:linear-gradient(135deg,#4c6a32 0%,#6b7d47 45%,#3e4c3a 100%)}

/* clients */
.clients{top:2240px;height:355px;background:var(--soft)}
.clients .section-title{position:absolute;top:46px;width:100%}
.clients .intro{position:absolute;top:104px;left:200px;width:800px;text-align:center;font-size:14px;line-height:26px;color:var(--grey)}
.client{position:absolute;top:193px;width:172px;height:86px;display:flex;align-items:center;justify-content:center;font-size:22px;font-weight:700;color:var(--ink)}
.client::before{content:"";position:absolute;inset:0;border:1px solid var(--line);background:var(--white);transform:skewX(-14deg);z-index:0}
.client span{position:relative;z-index:1}
.client-arrow{position:absolute;top:221px;width:20px;height:30px}

/* footer */
.site-footer{top:2595px;height:332px;background:var(--footer);color:#e6e6e6}
.fcol{position:absolute;top:54px}
.fcol h5{font-size:15.5px;font-weight:400;text-transform:uppercase;color:var(--white);margin-bottom:14px}
.fcol ul{list-style:none}
.fcol li{font-size:12.5px;line-height:30px;color:#dcdcdc;display:flex;align-items:center;gap:12px}
.socials{display:flex;gap:6px;margin-top:14px}
.socials span{width:38px;height:38px;border-radius:50%;background:var(--red);border:2px solid var(--white);display:block}
.footer-rule{position:absolute;left:100px;right:100px;top:257px;height:1px;background:#6a6a6a}
.copyright{position:absolute;left:100px;top:279px;font-size:12px;color:#dcdcdc}
</style>
</head>
<body>

<header class="site-header">
  <div class="brand">
    <span class="brand-mark"></span>
    <div class="brand-name">STEADFAST</div>
    <div class="brand-sub">CLEANING SERVICES</div>
  </div>
  <div class="call">
    <svg width="40" height="40" viewBox="0 0 40 40"><circle cx="20" cy="20" r="18" fill="none" stroke="var(--red)" stroke-width="2.5"/><path d="M14 11c1.5-1 2.5 0 3.5 2l1 2c.5 1 0 2-1 2.5l-1 .5c1 2.5 3 4.5 5.5 5.5l.5-1c.5-1 1.5-1.5 2.5-1l2 1c2 1 3 2 2 3.5-1.5 2.5-4 3-6.5 2-4.5-2-8-5.5-10-10-1-2.5-.5-5 1.5-7z" fill="var(--red)"/></svg>
    <span>Call Us: <span class="num">555-314-2760</span></span>
  </div>
  <a class="btn header-estimate">Free Estimate</a>
  <ul class="nav">
    <li class="active" style="left:0">HOME</li>
    <li style="left:96px">ABOUT US</li>
    <li style="left:219px">SERVICES</li>
    <li style="left:335px">WHAT WE DO</li>
    <li style="left:481px">BLOG</li>
    <li style="left:570px">CONTACT US</li>
  </ul>
</header>

<section class="hero">
  <div class="hero-photo" role="img" aria-label="Yellow mop bucket and wet floor caution signs in a commercial hallway"></div>
  <h1>COMMERCIAL JANITORIAL CLEANING COMPANY</h1>
  <p>We provide Janitorial cleaning particularly for commercial buildings</p>
  <a class="btn">Free Estimate</a>
  <svg class="slide-arrow prev" viewBox="0 0 38 46"><path d="M24 10L12 23l12 13" fill="none" stroke="#fff" stroke-opacity=".7" stroke-width="2.5"/></svg>
  <svg class="slide-arrow next" viewBox="0 0 38 46"><rect width="38" height="46" rx="19" fill="#fff" fill-opacity=".15"/><path d="M15 10l12 13-12 13" fill="none" stroke="#fff" stroke-opacity=".7" stroke-width="2.5"/></svg>
</section>

<section class="welcome">
  <h2 class="section-title">Welcome to Commercial Janitorial Cleaning Company</h2>
  <p class="intro">Lorem ipsum dolor sit amet, consectetur adipiscing elit, sed do eiusmod tempor incididunt ut labore et dolore magna aliqua. Ut enim ad minim veniam, quis nostrud exercitation ullamco laboris nisi ut aliquip ex ea commodo consequat</p>

  <div class="feature" style="left:82px">
    <div class="disc" style="background:var(--red);color:var(--red)">
      <svg width="60" height="60" viewBox="0 0 60 60" fill="#fff"><circle cx="24" cy="10" r="6"/><path d="M18 18h12l4 14h-5l-1 20h-5l-1-16-2 16h-5l1-20-3 4z"/><rect x="36" y="20" width="3" height="28" transform="rotate(-20 37 34)"/><rect x="40" y="46" width="14" height="6" rx="2"/></svg>
    </div>
    <h3>Best Cleaning</h3>
    <p>Sed ut perspiciatis unde omnis iste natus error sit voluptatem accusantium doloremque laudantium.</p>
  </div>
  <div class="feature" style="left:437px">
    <div class="disc" style="background:var(--blue);color:var(--blue)">
      <svg width="60" height="60" viewBox="0 0 60 60" fill="#fff"><rect x="10" y="26" width="10" height="24" rx="1"/><path d="M23 27l8-14c1-2 5-2 5 2l-2 10h12c3 0 5 3 4 5l-4 16c-1 2-2 4-5 4H23z"/></svg>
    </div>
    <h3>Quality Service</h3>
    <p>Sed ut perspiciatis unde omnis iste natus error sit voluptatem accusantium doloremque laudantium.</p>
  </div>
  <div class="feature" style="left:792px">
    <div class="disc" style="background:var(--green);color:var(--green)">
      <svg width="64" height="64" viewBox="0 0 64 64"><circle cx="36" cy="20" r="13" fill="#fff"/><text x="36" y="26" text-anchor="middle" font-family="Open Sans,sans-serif" font-weight="700" font-size="17" fill="var(--green)">$</text><path d="M6 42h10l8 3h10c3 0 3 4 0 4H24m-8 5l16 4 24-12c2-2 0-5-3-4l-13 5" fill="none" stroke="#fff" stroke-width="3.5" stroke-linecap="round" stroke-linejoin="round"/></svg>
    </div>
    <h3>Low Prices</h3>
    <p>Sed ut perspiciatis unde omnis iste natus error sit voluptatem accusantium doloremque laudantium.</p>
  </div>
</section>

<section class="services">
  <h2 class="section-title">What We Do</h2>
  <div class="pager"><span></span><span></span></div>

  <article class="card" style="left:100px">
    <div class="thumb" role="img" aria-label="Cleaner wiping an office desk" style="background:linear-gradient(135deg,#e6e4df,#8aa6b8 60%,#5c6870)"></div>
    <h4>General Office Cleaning</h4>
    <p>Sed ut perspiciatis unde omnis iste natus error sit voluptatem accusantium</p>
  </article>
  <article class="card" style="left:353px">
    <div class="thumb" role="img" aria-label="Worker cleaning solar panels at a construction site" style="background:linear-gradient(135deg,#6b4a3c,#3a4e7a 50%,#7b8fb3)"></div>
    <h4>Construction Cleaning</h4>
    <p>Sed ut perspiciatis unde omnis iste natus error sit voluptatem accusantium</p>
  </article>
  <article class="card" style="left:606px">
    <div class="thumb" role="img" aria-label="Vacuum cleaner on a beige carpet" style="background:linear-gradient(180deg,#e9e3d8,#cfc3b0)"></div>
    <h4>Carpet Extraction</h4>
    <p>Sed ut perspiciatis unde omnis iste natus error sit voluptatem accusantium</p>
  </article>
  <article class="card" style="left:859px">
    <div class="thumb" role="img" aria-label="Window cleaners on a glass office tower" style="background:linear-gradient(135deg,#2f86b8,#1e5f8c 60%,#3aa0c8)"></div>
    <h4>Consultation/Business</h4>
    <p>Sed ut perspiciatis unde omnis iste natus error sit voluptatem accusantium</p>
  </article>
</section>

<section class="about">
  <h2 class="section-title">About Us</h2>
  <div class="about-copy">
    <h3>Commercial Janitorial Cleaning Company</h3>
    <p class="lead">But I must explain to you how all this mistaken idea of denouncing pleasure and praising pain was born and I will give you a complete account of the system, and expound the actual teachings of the great explorer of the truth.</p>
    <ul class="ticks">
      <li><svg width="12" height="12" viewBox="0 0 12 12"><circle cx="6" cy="6" r="6" fill="var(--red)"/><path d="M3 6l2 2 4-4" fill="none" stroke="#fff" stroke-width="1.6"/></svg>Nisi ut aliquid ex ea commodi consequatur.</li>
      <li><svg width="12" height="12" viewBox="0 0 12 12"><circle cx="6" cy="6" r="6" fill="var(--red)"/><path d="M3 6l2 2 4-4" fill="none" stroke="#fff" stroke-width="1.6"/></svg>Vel illum qui dolorem eum fugiat quo voluptas nulla pariatur.</li>
      <li><svg width="12" height="12" viewBox="0 0 12 12"><circle cx="6" cy="6" r="6" fill="var(--red)"/><path d="M3 6l2 2 4-4" fill="none" stroke="#fff" stroke-width="1.6"/></svg>Quis autem vel eum iure reprehenderit qui in ea voluptate.</li>
    </ul>
  </div>
  <a class="btn">Learn More</a>
  <div class="family-photo" role="img" aria-label="Family photo of the owners outdoors by a ladder in an orchard"></div>
</section>

<section class="clients">
  <h2 class="section-title">Our Clients</h2>
  <p class="intro">At vero eos et accusamus et iusto odio dignissimos ducimus qui blanditiis praesentium voluptatum deleniti atque corrupti quos dolores et quas molestias excepturi sint occaecati cupiditate.</p>
  <svg class="client-arrow" style="left:80px" viewBox="0 0 20 30"><path d="M15 4L5 15l10 11" fill="none" stroke="#b5b5b5" stroke-width="3"/></svg>
  <div class="client" style="left:125px"><span>Norvale</span></div>
  <div class="client" style="left:322px"><span>Ridgeway</span></div>
  <div class="client" style="left:519px"><span>Bricklane</span></div>
  <div class="client" style="left:716px"><span>Tallstone</span></div>
  <div class="client" style="left:913px"><span>Halvern</span></div>
  <svg class="client-arrow" style="left:1100px" viewBox="0 0 20 30"><path d="M5 4l10 11L5 26" fill="none" stroke="#b5b5b5" stroke-width="3"/></svg>
</section>

<footer class="site-footer">
  <div class="fcol" style="left:100px">
    <h5>Company</h5>
    <ul><li>Home</li><li>About us</li><li>What We Do</li><li>Blog</li><li>Contact us</li></ul>
  </div>
  <div class="fcol" style="left:283px">
    <h5>Services</h5>
    <ul><li>Commercial</li><li>Constructions</li><li>Maintenance</li><li>Others</li></ul>
  </div>
  <div class="fcol" style="left:462px">
    <h5>Get in Touch</h5>
    <ul>
      <li><svg width="13" height="13" viewBox="0 0 14 14"><path d="M3 1c1-.5 1.5 0 2 1l1 2c.3.7 0 1.2-.6 1.5l-.6.3c.7 1.7 2 3 3.7 3.7l.3-.6c.3-.6.8-.9 1.5-.6l2 1c1 .5 1.5 1 1 2-1 1.7-2.7 2-4.3 1.3C5.7 11.3 3 8.7 1.5 5.5.8 3.9 1.3 2 3 1z" fill="#fff"/></svg>Call us on 555-314-2760</li>
      <li><svg width="13" height="11" viewBox="0 0 14 11"><rect width="14" height="11" rx="1" fill="#fff"/><path d="M0 1l7 5 7-5" fill="none" stroke="var(--footer)" stroke-width="1.3"/></svg>hello@steadfastclean.com</li>
    </ul>
  </div>
  <div class="fcol" style="left:769px">
    <h5>Why Us</h5>
    <ul><li>My Account</li><li>Team</li><li>Privacy &amp; Policy</li><li>FAQ</li></ul>
  </div>
  <div class="fcol" style="left:940px">
    <h5>Follow Us</h5>
    <ul><li>Please connect with us on</li></ul>
    <div class="socials"><span></span><span></span><span></span><span></span></div>
  </div>
  <div class="footer-rule"></div>
  <p class="copyright">© 2017 Steadfast Cleaning Services.&nbsp; All right reserved.&nbsp; Term of Use</p>
</footer>

</body>
</html>
```